Global Aviation Services website

we are a start up airline/aviation services company that will operate in Australia, USA and New Zealand initially. Fundamentally the service is to airlines who fly into and out of a market yet do not wish to have their own admin, sales and marketing infrastructures. They would use us.
The company name is Veltaro.
It needs to look sophisticated, sharp and professional. We would like it designed and built in the CMS - wordpress so we can update after the project is finished when necessary. An example of who we are and a good website we like can be found at: http://pembrikegroup.example/. There is no ecommerce or interactivity other than a contact us. We do like animation for promotion. There will be links to our airline clients and sub sites or pages will exist for the various offices we have globally. Currently 6. Each of these offices will have a dedicated local URL. Please submit your suggestion of a home page and 2 internal pages. Thank you and kind regards Miriam
Target Market(s)
airlines, airline technology companies,
Industry/Entity Type
Aviation
Coding
Coded - Design and coding required
Number of Pages Required
5+ page
Look and feel

```html
<!DOCTYPE html>
<html lang="en">
<head>
<meta charset="utf-8">
<title>Veltaro — Contact Us</title>
<link href="https://fonts.googleapis.com/css2?family=Raleway:wght@300;400;600;700&family=Open+Sans:wght@400;600&display=swap" rel="stylesheet">
<style>
:root{
  --brand:#0c57a7;
  --brand-dark:#0a4a8f;
  --ink:#1c1c2a;
  --muted:#8a8a8a;
  --field-line:#cfcfcf;
  --select-bg:#efefef;
  --white:#ffffff;
  --sky-top:#8aa3b8;
  --sky-bottom:#4e6f8c;
  --map-light:#ececec;
  --map-dark:#cfcfcf;
}
*{box-sizing:border-box;margin:0;padding:0}
html,body{width:1200px;height:1089px;overflow:hidden;background:var(--white)}
body{position:relative;font-family:"Open Sans",sans-serif;color:var(--ink)}
.abs{position:absolute}

/* header */
.site-header{position:absolute;left:0;top:0;width:1200px;height:66px;background:var(--white)}
.brand-name{position:absolute;left:89px;top:14px;font-family:"Raleway",sans-serif;font-weight:700;font-size:30px;color:var(--brand);letter-spacing:1px;line-height:38px}
.main-nav{position:absolute;left:0;top:0;height:66px}
.main-nav a{position:absolute;top:0;height:66px;line-height:68px;font-family:"Open Sans",sans-serif;font-size:12px;color:var(--ink);text-decoration:none;white-space:nowrap}
.main-nav .is-active{background:var(--brand);color:var(--white);font-weight:700;width:75px;text-align:center}
.search-icon{position:absolute;left:1096px;top:25px}

/* hero */
.hero{position:absolute;left:0;top:66px;width:1200px;height:117px;overflow:hidden}
.hero-photo{position:absolute;inset:0;background:linear-gradient(180deg,var(--sky-top),var(--sky-bottom) 60%,#7c93a8)}
.hero-band{position:absolute;inset:0}
.hero-title{position:absolute;left:89px;top:44px;font-family:"Raleway",sans-serif;font-weight:700;font-size:31px;color:var(--white);line-height:40px}

/* location filters */
.filter{position:absolute;top:220px;width:225px;height:40px;background:var(--select-bg);border:1px solid #dcdcdc;font-size:12px;color:#666;line-height:38px;padding-left:17px}
.filter::after{content:"";position:absolute;right:10px;top:17px;border-left:3px solid transparent;border-right:3px solid transparent;border-top:5px solid #333}

.office-map{position:absolute;left:89px;top:283px;width:1022px;height:360px;background:linear-gradient(135deg,var(--map-light),var(--map-dark) 50%,var(--map-light))}

/* contact section */
.section-title{position:absolute;left:89px;top:668px;font-family:"Raleway",sans-serif;font-weight:400;font-size:28px;line-height:36px;color:var(--ink)}
.section-title strong{font-weight:700;color:var(--brand)}
.title-rule{position:absolute;left:89px;top:702px;width:21px;height:3px;background:var(--brand)}

.field{position:absolute;border:2px solid var(--field-line);font-size:14px;color:var(--muted);padding-left:14px;line-height:42px;background:var(--white)}
.send-btn{position:absolute;left:89px;top:959px;width:122px;height:43px;border:2px solid var(--brand);color:var(--brand);font-size:14px;text-align:center;line-height:39px}

.world-map{position:absolute;left:640px;top:712px;width:560px;height:250px;background:radial-gradient(ellipse at 50% 50%,rgba(0,0,0,0.035),rgba(0,0,0,0) 70%)}
.contact-item{position:absolute;left:677px;width:420px;height:60px}
.contact-item .ring{position:absolute;left:0;top:0;width:60px;height:60px;border:2px solid var(--brand);border-radius:50%;display:flex;align-items:center;justify-content:center}
.contact-item .label{position:absolute;left:71px;top:0;line-height:60px;font-size:14px;color:var(--muted)}

/* footer */
.site-footer{position:absolute;left:0;top:1036px;width:1200px;height:53px;background:var(--brand);color:var(--white);font-size:12px;line-height:53px}
.site-footer .copy{position:absolute;left:89px}
.site-footer .legal{position:absolute;right:89px}
.site-footer .sep{margin:0 14px}
</style>
</head>
<body>

<header class="site-header">
  <div class="brand-name">Veltaro</div>
  <nav class="main-nav">
    <a style="left:817px">HOME</a>
    <a style="left:878px">ABOUT</a>
    <a style="left:942px">NEW</a>
    <a class="is-active" style="left:997px">CONTACT</a>
  </nav>
  <svg class="search-icon" width="16" height="16" viewBox="0 0 16 16" aria-hidden="true">
    <circle cx="6" cy="6" r="4.5" fill="none" stroke="#1c1c2a" stroke-width="1.8"/>
    <line x1="9.5" y1="9.5" x2="14.5" y2="14.5" stroke="#1c1c2a" stroke-width="2.4" stroke-linecap="round"/>
  </svg>
</header>

<section class="hero">
  <div class="hero-photo" role="img" aria-label="Aerial photograph of clouds over the sea"></div>
  <svg class="hero-band" width="1200" height="117" aria-hidden="true">
    <polygon points="0,0 402,0 466,117 0,117" fill="#0c57a7"/>
  </svg>
  <h1 class="hero-title">CONTACT US</h1>
</section>

<div class="filter" style="left:89px">Select Country</div>
<div class="filter" style="left:338px">Select State</div>
<div class="filter" style="left:586px">Select City</div>

<div class="office-map" role="img" aria-label="Street map of central Montreal with red pins marking office locations"></div>

<h2 class="section-title">Contact <strong>Us</strong></h2>
<div class="title-rule"></div>

<div class="field" style="left:89px;top:728px;width:261px;height:46px">Your Name...</div>
<div class="field" style="left:367px;top:728px;width:261px;height:46px">Your Phone Number...</div>
<div class="field" style="left:89px;top:784px;width:540px;height:46px">Your Email..</div>
<div class="field" style="left:89px;top:841px;width:540px;height:104px;line-height:20px;padding-top:12px">Your Message</div>
<div class="send-btn">SEND</div>

<div class="world-map" role="img" aria-label="Faint world map in the background"></div>

<div class="contact-item" style="top:728px">
  <div class="ring">
    <svg width="14" height="18" viewBox="0 0 14 18" aria-hidden="true"><path d="M7 1a5.5 5.5 0 0 0-5.5 5.5C1.5 11 7 17 7 17s5.5-6 5.5-10.5A5.5 5.5 0 0 0 7 1zm0 7.6a2.1 2.1 0 1 1 0-4.2 2.1 2.1 0 0 1 0 4.2z" fill="#0c57a7"/></svg>
  </div>
  <div class="label">Some address line here...</div>
</div>
<div class="contact-item" style="top:806px">
  <div class="ring">
    <svg width="16" height="12" viewBox="0 0 16 12" aria-hidden="true"><rect x="0.5" y="0.5" width="15" height="11" fill="#0c57a7"/><polyline points="1,1 8,7 15,1" fill="none" stroke="#fff" stroke-width="1.2"/></svg>
  </div>
  <div class="label">info@veltaro.example</div>
</div>
<div class="contact-item" style="top:884px">
  <div class="ring">
    <svg width="14" height="14" viewBox="0 0 24 24" aria-hidden="true"><path d="M6.6 10.8a15.1 15.1 0 0 0 6.6 6.6l2.2-2.2a1 1 0 0 1 1-.25 11.4 11.4 0 0 0 3.6.57 1 1 0 0 1 1 1V20a1 1 0 0 1-1 1A17 17 0 0 1 3 4a1 1 0 0 1 1-1h3.5a1 1 0 0 1 1 1c0 1.25.2 2.45.57 3.57a1 1 0 0 1-.25 1z" fill="#0c57a7"/></svg>
  </div>
  <div class="label">555-014-2768</div>
</div>

<footer class="site-footer">
  <span class="copy">©2016 Veltaro, All Rights Reserved</span>
  <span class="legal">Privacy Policy<span class="sep">|</span>Terms &amp; Conditions</span>
</footer>

</body>
</html>
```